Medical VIP club - small design

Please read the specs in a design brief attached. Also we don't have logo in a Vector format and attaching the only version we have.

Industry/Entity Type

Club

```html
<!DOCTYPE html>
<html lang="en">
<head>
<meta charset="utf-8">
<title>Calvora — VIP Club</title>
<link href="https://fonts.googleapis.com/css2?family=Exo+2:wght@300;400;600;700&display=swap" rel="stylesheet">
<style>
  :root {
    --bar-dark: #1f1607;
    --brown: #6b5a42;
    --brown-deep: #2a1f0e;
    --cream: #efeadb;
    --text-light: #f1eadb;
    --phone-ink: #2a2010;
    --tab-top: #5b4b36;
    --tab-bottom: #241a0c;
    --tab-edge: #8b7a60;
    --card-head-top: #3a2d18;
    --card-head-bottom: #171005;
    --overlay: rgba(28, 20, 8, 0.82);
    --footer-mark: #5d4d35;
  }
  * { box-sizing: border-box; margin: 0; padding: 0; }
  html, body { width: 1200px; height: 950px; overflow: hidden; }
  body {
    position: relative;
    background: var(--brown);
    font-family: "Exo 2", sans-serif;
    color: var(--text-light);
  }
  .top-bar { position: absolute; left: 0; top: 0; width: 1200px; height: 17px; background: var(--bar-dark); }
  .header-backdrop {
    position: absolute; left: 0; top: 17px; width: 1200px; height: 518px;
    background:
      radial-gradient(ellipse 420px 520px at 600px 200px, rgba(107,90,66,0.9), rgba(107,90,66,0) 70%),
      linear-gradient(180deg, #6e5c43 0%, #5a4932 35%, #3b2d17 70%, var(--brown-deep) 100%);
  }
  .brand { position: absolute; left: 145px; top: 48px; display: flex; align-items: center; gap: 12px; }
  .brand-dot { width: 30px; height: 30px; border-radius: 50%; background: var(--text-light); }
  .brand-name { font-size: 40px; font-weight: 600; color: var(--text-light); line-height: 1; letter-spacing: 0.5px; }
  .phone {
    position: absolute; right: 140px; top: 60px;
    font-size: 30px; font-weight: 300; color: var(--phone-ink); letter-spacing: 0.5px;
  }
  .main-nav { position: absolute; left: 0; top: 132px; width: 1200px; height: 41px; }
  .tab {
    position: absolute; top: 0; height: 41px;
    display: flex; align-items: center; justify-content: center;
    font-size: 19px; color: var(--text-light); text-decoration: none; white-space: nowrap;
    letter-spacing: -0.2px;
    background: linear-gradient(180deg, var(--tab-top), var(--tab-bottom));
    border: 1px solid var(--tab-edge); border-bottom: none;
    clip-path: polygon(0 0, calc(100% - 14px) 0, 100% 14px, 100% 100%, 0 100%);
  }
  .hero-frame {
    position: absolute; left: 114px; top: 173px; width: 960px; height: 400px;
    background: var(--cream); box-shadow: 0 6px 14px rgba(0,0,0,0.35);
  }
  .hero-photo {
    position: absolute; left: 8px; top: 8px; width: 944px; height: 384px;
    background:
      radial-gradient(ellipse 180px 260px at 470px 200px, rgba(250,200,120,0.55), rgba(250,200,120,0) 70%),
      linear-gradient(90deg, #7a1a0c 0%, #b8231a 10%, #3a2410 24%, #c9a060 40%, #e8c080 50%, #9a5a20 60%, #2a1a0c 72%, #b82418 88%, #6a1608 100%);
  }
  .hero-caption {
    position: absolute; left: 593px; top: 8px; width: 288px; height: 208px; background: var(--overlay);
  }
  .hero-title { position: absolute; left: 11px; top: 58px; font-size: 56px; font-weight: 700; line-height: 1; white-space: nowrap; }
  .hero-sub { position: absolute; left: 14px; top: 120px; font-size: 21px; font-weight: 400; line-height: 25px; white-space: nowrap; }
  .hero-go { position: absolute; left: 208px; top: 124px; }
  .slide-arrow { position: absolute; top: 333px; width: 40px; height: 68px; background: var(--cream); display: flex; align-items: center; justify-content: center; }
  .slide-arrow.prev { left: 118px; border-radius: 0 34px 34px 0; }
  .slide-arrow.next { left: 1032px; border-radius: 34px 0 0 34px; }
  .service-card {
    position: absolute; top: 613px; width: 181px; height: 181px;
    border-radius: 3px; overflow: hidden; background: var(--card-head-bottom);
    box-shadow: 0 2px 4px rgba(0,0,0,0.3);
  }
  .card-title {
    height: 37px; display: flex; align-items: center; justify-content: center;
    font-size: 15.5px; letter-spacing: -0.4px; white-space: nowrap; line-height: 1;
    padding-bottom: 2px;
    background: linear-gradient(180deg, var(--card-head-top), var(--card-head-bottom));
  }
  .card-photo { height: 133px; }
  .site-footer { position: absolute; left: 0; top: 831px; width: 1200px; height: 119px; background: var(--bar-dark); }
  .footer-brand { position: absolute; left: 160px; top: 35px; display: flex; align-items: center; gap: 8px; }
  .footer-brand .brand-dot { width: 22px; height: 22px; background: var(--footer-mark); }
  .footer-brand .brand-name { font-size: 28px; color: var(--footer-mark); }
  .copyright { position: absolute; left: 333px; top: 27px; font-family: Arial, Helvetica, sans-serif; font-size: 12px; color: #ffffff; white-space: nowrap; }
  .social { position: absolute; left: 973px; top: 21px; display: flex; gap: 9px; }
  .social span { width: 24px; height: 24px; border-radius: 3px; background: linear-gradient(180deg, #a9a696, #6f6c5e); }
</style>
</head>
<body>
  <div class="top-bar"></div>
  <div class="header-backdrop" role="img" aria-label="Brown backdrop with faint damask ornament on both sides"></div>

  <div class="brand"><span class="brand-dot"></span><span class="brand-name">calvora</span></div>
  <div class="phone">555-010-0199</div>

  <nav class="main-nav">
    <a class="tab" style="left:122px;width:97px">Home</a>
    <a class="tab" style="left:221px;width:117px">About Us</a>
    <a class="tab" style="left:339px;width:112px">VIP Club</a>
    <a class="tab" style="left:452px;width:107px">Services</a>
    <a class="tab" style="left:560px;width:210px">Packages and Prices</a>
    <a class="tab" style="left:771px;width:142px">Registration</a>
    <a class="tab" style="left:915px;width:112px">Contacts</a>
  </nav>

  <section class="hero-frame">
    <div class="hero-photo" role="img" aria-label="Luxurious hotel corridor with red glass panels and gold frames"></div>
    <div class="hero-caption">
      <div class="hero-title">VIP Club</div>
      <div class="hero-sub">Reserve Your<br>Membership Today</div>
      <svg class="hero-go" width="26" height="40" viewBox="0 0 26 40"><path d="M5 2 L22 20 L5 38 L1 34 L14 20 L1 6 Z" fill="#f1eadb"/></svg>
    </div>
  </section>

  <div class="slide-arrow prev"><svg width="18" height="30" viewBox="0 0 18 30"><path d="M14 1 L2 15 L14 29 L17 26 L8 15 L17 4 Z" fill="#1f1607"/></svg></div>
  <div class="slide-arrow next"><svg width="18" height="30" viewBox="0 0 18 30"><path d="M4 1 L16 15 L4 29 L1 26 L10 15 L1 4 Z" fill="#1f1607"/></svg></div>

  <div class="service-card" style="left:122px">
    <div class="card-title">Emergency Services</div>
    <div class="card-photo" role="img" aria-label="Ambulance with lights at night" style="background:linear-gradient(160deg,#d8c8a8,#8a7a62 45%,#2a2218 80%)"></div>
  </div>
  <div class="service-card" style="left:312px">
    <div class="card-title">Transportation Services</div>
    <div class="card-photo" role="img" aria-label="Aircraft cabin interior" style="background:linear-gradient(160deg,#e4ddd0,#9a9284 45%,#1e1a14 85%)"></div>
  </div>
  <div class="service-card" style="left:502px">
    <div class="card-title">Hotel Services</div>
    <div class="card-photo" role="img" aria-label="Grand hotel entrance with red carpet" style="background:linear-gradient(180deg,#5a1810,#c8a070 40%,#e8d2a8 60%,#8a3020)"></div>
  </div>
  <div class="service-card" style="left:692px">
    <div class="card-title">Medical Professionals</div>
    <div class="card-photo" role="img" aria-label="Doctor in green scrubs with crossed arms" style="background:linear-gradient(180deg,#2a3a1a,#5a8a3a 45%,#3e6a2a 80%,#1e2a12)"></div>
  </div>
  <div class="service-card" style="left:882px">
    <div class="card-title">Become a Member</div>
    <div class="card-photo" role="img" aria-label="Marble staircase with a red velvet rope" style="background:linear-gradient(135deg,#f2ece0,#d8ccb4 45%,#8a5a40 75%,#5a1818)"></div>
  </div>

  <footer class="site-footer">
    <div class="footer-brand"><span class="brand-dot"></span><span class="brand-name">calvora</span></div>
    <div class="copyright">Copyright 2010 Calvora. All rights reserved.</div>
    <div class="social" aria-label="Social links"><span></span><span></span><span></span></div>
  </footer>
</body>
</html>
```